Ember Fold Whiskey Label

We are looking for a label to be made for our single batch whiskey. in the attached pdf you will see the lay out of the design. We are going to use a whiskey bottle with a cork. Some of the label you will need to leave some space for hand writing.

Target Market(s)

people who like craft beer and whiskey

Industry/Entity Type

Craft Distillery

Font styles to use
Decorative

Colors

Designer to choose colors to be used in the design.

Requirements
Must have
• room for hand writing informatiom

```html
<!DOCTYPE html>
<html lang="en">
<head>
<meta charset="utf-8">
<title>Ember Fold Whiskey Label</title>
<link href="https://fonts.googleapis.com/css2?family=Open+Sans:wght@400;600;700&family=Caveat:wght@500&display=swap" rel="stylesheet">
<style>
  :root {
    --backdrop: #ad8736;
    --paper: #f3f0ea;
    --ink: #1c1a18;
    --gold: #dcb46c;
    --script-ink: #2d3b9c;
    --band: #141414;
    --band-text: #f3f0ea;
  }
  * { box-sizing: border-box; margin: 0; padding: 0; }
  html, body { width: 1000px; height: 1200px; overflow: hidden; }
  body {
    background: var(--backdrop);
    font-family: "Open Sans", Arial, sans-serif;
    color: var(--ink);
    position: relative;
  }
  .label {
    position: absolute;
    left: 210px;
    top: 60px;
    width: 580px;
    height: 1080px;
    background: var(--paper);
  }
  .distillery-name {
    position: absolute;
    top: 82px;
    left: 0;
    width: 100%;
    text-align: center;
    font-size: 34px;
    letter-spacing: 0.5px;
    font-weight: 600;
  }
  .ornament {
    position: absolute;
    top: 160px;
    left: 45px;
    width: 490px;
    height: 44px;
    background: linear-gradient(90deg, rgba(220,180,108,0) 0%, rgba(220,180,108,0.55) 25%, var(--gold) 50%, rgba(220,180,108,0.55) 75%, rgba(220,180,108,0) 100%);
    border-radius: 22px;
  }
  .product-name {
    position: absolute;
    top: 236px;
    left: 0;
    width: 100%;
    text-align: center;
    font-family: "Open Sans", Arial, sans-serif;
    font-weight: 700;
    font-size: 92px;
    line-height: 120px;
    letter-spacing: -1px;
    color: var(--ink);
  }
  .spirit-band {
    position: absolute;
    top: 388px;
    left: 38px;
    width: 504px;
    height: 56px;
    background: var(--band);
    color: var(--band-text);
    font-size: 26px;
    line-height: 56px;
    text-align: center;
    letter-spacing: -0.3px;
  }
  .gold-rule {
    position: absolute;
    left: 38px;
    width: 504px;
    height: 13px;
    background: var(--gold);
  }
  .gold-rule.top { top: 478px; }
  .gold-rule.bottom { top: 852px; }
  .thin-rule {
    position: absolute;
    left: 38px;
    width: 504px;
    height: 2px;
    background: var(--gold);
  }
  .thin-rule.first { top: 606px; }
  .thin-rule.second { top: 754px; }
  .column-divider {
    position: absolute;
    left: 286px;
    top: 607px;
    width: 2px;
    height: 246px;
    background: var(--gold);
  }
  .field-label {
    position: absolute;
    font-size: 21px;
    letter-spacing: -0.2px;
  }
  .field-entry {
    position: absolute;
    font-family: "Caveat", cursive;
    font-size: 36px;
    color: var(--script-ink);
    white-space: nowrap;
  }
  .maker-block {
    position: absolute;
    top: 912px;
    left: 40px;
    width: 400px;
    font-size: 20px;
    line-height: 1.25;
  }
  .maker-block .maker-lines { font-weight: 700; }
  .maker-block .maker-address { font-size: 16px; margin-top: 4px; }
  .volume-badge {
    position: absolute;
    top: 934px;
    left: 462px;
    width: 76px;
    height: 76px;
  }
</style>
</head>
<body>
  <section class="label">
    <h2 class="distillery-name">IRON SPUR DISTILLERY</h2>
    <div class="ornament" role="img" aria-label="Gold scrolled flourish ornament"></div>
    <h1 class="product-name">Ember Fold</h1>
    <div class="spirit-band">Spirits Distilled From Malt Mash and Hops</div>

    <div class="gold-rule top"></div>

    <span class="field-label" style="top:516px;left:40px;">Distillate Source:</span>
    <span class="field-entry" style="top:546px;left:100px;">Vivamus dolor justo, mattis vel</span>

    <div class="thin-rule first"></div>
    <div class="column-divider"></div>

    <span class="field-label" style="top:622px;left:40px;">Aged:</span>
    <span class="field-entry" style="top:668px;left:56px;">Lorem ipsum dolor</span>

    <span class="field-label" style="top:630px;left:304px;">% ALC. BY VOL.</span>
    <span class="field-entry" style="top:672px;left:350px;">Consectetur</span>

    <div class="thin-rule second"></div>

    <span class="field-label" style="top:770px;left:40px;">BOTTLE:</span>
    <span class="field-entry" style="top:800px;left:66px;">Adipiscing elit</span>

    <span class="field-label" style="top:782px;left:304px;">OF:</span>
    <span class="field-entry" style="top:804px;left:356px;">Non mollis</span>

    <div class="gold-rule bottom"></div>

    <div class="maker-block">
      <div class="maker-lines">DISTILLED AND BOTTLE BY<br>IRON SPUR DISTILLERY LLC</div>
      <div class="maker-address">48 HARLOW ST. FAIRHAVEN NJ 08120</div>
    </div>

    <svg class="volume-badge" viewBox="0 0 76 76" aria-label="750ML">
      <rect x="14" y="14" width="48" height="48" rx="6" transform="rotate(45 38 38)" fill="#1c1a18"/>
      <text x="38" y="43" text-anchor="middle" fill="#f3f0ea" font-family="Open Sans, Arial, sans-serif" font-weight="700" font-size="14">750ML</text>
    </svg>
  </section>
</body>
</html>
```